Creative, fresh business card design for Orrin Linings

We need a fresh, creative business card design for Orrin Linings. We are the manufacturer of Orrin Linings in Australia. Wall panels are 2400 x 1200mm panels made from MDF and feature 3D patterns on the face of the panel. The colours to be used are green, silver/grey and white RGB
Red 187
Green 207
Blue 65.

An idea is to possibly use a watermark of one of our designs as a background (like on the "Ferns" design on the left hand side of page 2 of our brochure).

Target Market(s)

Interior designers, architects, builders and home renovators

Industry/Entity Type

Business

Contact Information for Business Card

Details to go on the card are:
Our logo (attached),
Slogan: "Decorative panels for interiors and exteriors",
Contact name,
Position,
Mobile phone number,
Business address,
Business phone,
Business fax,
Website and
Email address.

I have attached a few images of our panels and our brochure for reference.

The colours of the business card should feature our logo colours which are: RGB
Red 187
Green 207
Blue 65

Requirements
Must have
• Very modern fonts and design. Some of the designs shown especially the "Weave" design which is a popular design.
Nice to have
• Creative but simple design. Very contemporary.
Should not have
• Anything ornate or old fashioned.

```html
<!DOCTYPE html>
<html lang="en">
<head>
<meta charset="utf-8">
<title>Orrin Linings – Business Card</title>
<link href="https://fonts.googleapis.com/css2?family=Open+Sans:wght@300;400;600;700&display=swap" rel="stylesheet">
<style>
  :root {
    --brand-green: rgb(187, 207, 65);
    --green-deep: #98b52a;
    --green-light: #c9de5a;
    --silver: #9a9b9e;
    --ink: #555659;
    --ink-soft: #8d8e91;
    --card-white: #ffffff;
    --backdrop: #2a2a2a;
  }
  html, body {
    margin: 0;
    width: 1200px;
    height: 1000px;
    overflow: hidden;
    background: var(--backdrop);
    font-family: "Open Sans", Arial, sans-serif;
  }
  .card {
    position: absolute;
    left: 110px;
    top: 220px;
    width: 980px;
    height: 560px;
    border-radius: 40px;
    overflow: hidden;
    background: var(--card-white);
  }
  .band-top {
    position: absolute;
    left: 0; top: 0;
    width: 100%; height: 250px;
    background: linear-gradient(120deg, var(--green-light) 0%, var(--brand-green) 35%, var(--green-deep) 75%, var(--brand-green) 100%);
  }
  .band-bottom {
    position: absolute;
    left: 0; bottom: 0;
    width: 100%; height: 80px;
    background: linear-gradient(100deg, var(--green-deep) 0%, var(--brand-green) 50%, var(--green-light) 100%);
  }
  .brand {
    position: absolute;
    left: 120px;
    top: 120px;
    display: flex;
    align-items: center;
    gap: 18px;
  }
  .brand-square {
    width: 60px; height: 60px;
    background: var(--card-white);
  }
  .brand-name {
    color: var(--card-white);
    font-weight: 600;
    font-size: 50px;
    line-height: 1;
  }
  .slogan {
    position: absolute;
    left: 198px;
    top: 192px;
    color: var(--card-white);
    font-size: 18px;
    letter-spacing: 3px;
    line-height: 1.25;
  }
  .person {
    position: absolute;
    right: 540px;
    top: 280px;
    text-align: right;
  }
  .person-name {
    font-size: 36px;
    font-weight: 700;
    color: var(--ink);
    line-height: 1.1;
  }
  .person-name .surname { color: var(--brand-green); }
  .person-role {
    font-size: 20px;
    color: var(--ink);
    margin-bottom: 18px;
  }
  .person-address {
    font-size: 19px;
    color: var(--ink-soft);
    line-height: 1.3;
  }
  .divider {
    position: absolute;
    left: 470px;
    top: 272px;
    width: 2px;
    height: 180px;
    background: var(--brand-green);
  }
  .contacts {
    position: absolute;
    left: 500px;
    top: 270px;
    margin: 0; padding: 0;
    list-style: none;
  }
  .contacts li {
    display: flex;
    align-items: center;
    gap: 16px;
    height: 36px;
    font-size: 21px;
    color: var(--ink);
  }
  .contacts svg {
    width: 20px; height: 20px;
    fill: none;
    stroke: var(--brand-green);
    stroke-width: 2;
  }
</style>
</head>
<body>
  <div class="card">
    <div class="band-top" role="img" aria-label="Green faceted panel texture"></div>
    <div class="band-bottom" role="img" aria-label="Green faceted panel texture"></div>

    <div class="brand">
      <div class="brand-square"></div>
      <div class="brand-name">Orrin Linings</div>
    </div>
    <div class="slogan">decorative panels for<br>interiors &amp; landscapes</div>

    <div class="person">
      <div class="person-name">Tobin <span class="surname">Hale</span></div>
      <div class="person-role">Director</div>
      <div class="person-address">14 Carrow Street<br>Larkvale, 4821</div>
    </div>

    <div class="divider"></div>

    <ul class="contacts">
      <li><svg viewBox="0 0 20 20"><rect x="6" y="2" width="8" height="16" rx="1.5"/><line x1="9" y1="15" x2="11" y2="15"/></svg>+000 123 456 789</li>
      <li><svg viewBox="0 0 20 20"><path d="M4 3 L7 3 L8.5 7 L6.5 8.5 Q8 12 11.5 13.5 L13 11.5 L17 13 L17 16 Q10 17 4 10 Q3 6 4 3 Z"/></svg>+000 123 456 789</li>
      <li><svg viewBox="0 0 20 20"><rect x="3" y="8" width="14" height="8" rx="1"/><rect x="6" y="3" width="8" height="5"/><line x1="7" y1="12" x2="13" y2="12"/></svg>+000 123 456 789</li>
      <li><svg viewBox="0 0 20 20"><rect x="2" y="5" width="16" height="11"/><polyline points="2,5 10,11 18,5"/></svg>tobin@orrinlinings.au</li>
      <li><svg viewBox="0 0 20 20"><circle cx="11" cy="8" r="5"/><line x1="7.5" y1="11.5" x2="3" y2="17"/></svg>www.orrinlinings.au</li>
    </ul>
  </div>
</body>
</html>
```